Kestavo Estates is a commercial real estate development company based in the United States. We develop high-end office buildings and student housing apartments. We have a new logo and need to update all of our stationary items and business cards. We would like the design to be clean and professional. Our logo and color information is attached. Our logo MUST be in full color and not as white. It is preferred that the logo is on a white background.

Color code Blue R 0. G 62. B 124 ( #003E7C )
C 100 M84 Y 26 K 22
Black R32. G30. B30 ( #201E1E)
C100 M100 Y100 K100

Font used TRAJAN PRO3 PRO BOLD.

Items needed:
1. Business card - Leaning towards doing just a one side business card in a thicker paper. Include - logo, name - Peter T. Vance, Title - Chairman & CEO, 1870 Pembrook Blvd. Suite 400, Atlanta, GA 30127 - Cell number 404.555.####, Office 770.555.02## email@kestavoestates.com; www.kestavoestates.com.

2. Letterhead - Standard 8.5 by 11 paper. We do have a smaller size for the CEO that is 7.25 by 10.5 that is just a mirror of the letterhead except with his name (Peter T. Vance) and title (Chariman & CEO) listed at the top in the header. Letthead needs address, phone number and website, plus logo. *Prepared such that we can either implement as a Google Document template or professionally print.

3. Legal sized envelope - #10 envelope - which measures 4 1/8" by 9 1/2". We also use the same size envelope with a window. Need logo and address. A photo of the old envelope style is attached.

4. 9" x 12" Pocket folder - Need a design that can also be split to be a cover page and back - We use the cover pages in spiral binding machine, so we need to leave room on the left for that. One of the pockets should hold a business card. Include logo, address, phone, website. Also if text is needed, we could say development / leasing / property management.

5. Shipping label - 3 1/3" x 4" inches and 6 per page. Just need logo and address listed at top of the label and white space at bottom.

Company: Kestavo Estates
Address: 1870 Pembrook Blvd. Suite 400, Atlanta, GA 30127
Phone: 770.555.0214
Fax: 770.555.0287 (probably not needed)
Website: www.kestavoestates.com

Thank you for all your help!

Target Market(s)

Should communicate a strong corporate feel

Contact Information for Business Card

Include - logo, name - Peter T. Vance, Title - Chairman & CEO, 1870 Pembrook Blvd. Suite 400, Atlanta, GA 30127 - Cell number 404.555.####, Office 770.555.02## email@kestavoestates.com; www.kestavoestates.com.

Logo Text

Kestavo Estates

Colors

Requirements
Must have
• Our logo MUST be in full color and not as white. It is preferred that the logo is on a white background.
• Colors - Color code Blue R 0. G 62. B 124 ( #003E7C )
• C 100 M84 Y 26 K 22
Nice to have
• Font used in logo TRAJAN PRO3 PRO BOLD. Would love to see options of both a one sided and double-sided.
Should not have
• Logo in white.

```html
<!DOCTYPE html>
<html lang="en">
<head>
<meta charset="utf-8">
<title>Kestavo Estates — Letterhead</title>
<link rel="stylesheet" href="https://fonts.googleapis.com/css2?family=Cinzel:wght@400;700&family=Arimo:wght@400&display=swap">
<style>
  :root{
    --brand-blue:#003E7C;
    --brand-black:#201E1E;
    --body-grey:#5f5f5f;
    --paper:#ffffff;
    --backdrop:#b9cde6;
    --sig-tone:#dfe2e7;
  }
  *{box-sizing:border-box;margin:0;padding:0}
  html,body{width:1200px;height:784px;overflow:hidden}
  body{background:var(--backdrop);position:relative;font-family:"Arimo",Arial,sans-serif}

  .letterhead{
    position:absolute;left:314px;top:22px;width:572px;height:740px;
    background:var(--paper);
    box-shadow:0 6px 18px rgba(30,50,90,.25);
    border-top:6px solid var(--brand-blue);
  }

  .header{position:absolute;right:52px;top:34px;display:flex;align-items:center;gap:12px}
  .brand-dot{width:44px;height:44px;border-radius:50%;background:var(--brand-blue);flex:none}
  .brand-block{display:flex;flex-direction:column}
  .brand-name{font-family:"Cinzel",serif;font-weight:700;color:var(--brand-blue);font-size:22px;letter-spacing:1px;line-height:1.1}
  .exec-name{font-family:"Cinzel",serif;font-weight:700;color:var(--brand-blue);font-size:12px;letter-spacing:.5px;margin-top:6px;padding-top:5px;border-top:1px solid var(--brand-blue)}
  .exec-title{font-family:"Cinzel",serif;font-weight:400;color:var(--brand-blue);font-size:10px;letter-spacing:.6px;margin-top:2px}

  .body-copy{position:absolute;left:60px;top:140px;width:440px;color:var(--body-grey);font-size:10px;line-height:1.45}
  .body-copy p{margin-bottom:14px;text-indent:26px}
  .body-copy p:first-child{text-indent:0}

  .signature{position:absolute;left:60px;top:500px;width:130px;height:42px;background:var(--sig-tone);border-radius:4px}

  .footer{position:absolute;left:0;right:0;bottom:0}
  .contact-row{display:flex;align-items:center;justify-content:space-between;padding:0 14px 6px;font-family:"Cinzel",serif;font-size:6.6px;color:var(--brand-blue);letter-spacing:.2px;white-space:nowrap}
  .contact-item{display:flex;align-items:center;gap:3px}
  .contact-item svg{width:8px;height:8px;flex:none}
  .rule-thin{height:2px;background:var(--brand-blue);margin:0 0 3px}
  .rule-band{display:flex;height:9px}
  .rule-band .blue{flex:1;background:var(--brand-blue)}
  .rule-band .black{width:120px;background:var(--brand-black)}
</style>
</head>
<body>
  <main class="letterhead">
    <header class="header">
      <span class="brand-dot"></span>
      <div class="brand-block">
        <span class="brand-name">KESTAVO ESTATES</span>
        <span class="exec-name">PETER T. VANCE</span>
        <span class="exec-title">CHAIRMAN &amp; CEO</span>
      </div>
    </header>

    <section class="body-copy">
      <p>Lorem Ipsum is simply dummy text of the printing and typesetting industry. Lorem Ipsum has been the industry's standard dummy text ever since the 1500s, when an unknown printer took a galley of type and scrambled it to make a type specimen book. It has survived not only five centuries, but also the leap into electronic typesetting, remaining essentially unchanged. It was popularised in the 1960s with the release of Typeline sheets containing Lorem Ipsum passages, and more recently with desktop publishing software like Quillset Layout including versions of Lorem Ipsum.</p>
      <p>It is a long established fact that a reader will be distracted by the readable content of a page when looking at its layout. The point of using Lorem Ipsum is that it has a more-or-less normal distribution of letters, as opposed to using 'Content here, content here', making it look like readable English. Many desktop publishing packages and web page editors now use Lorem Ipsum as their default model text, and a search for 'lorem ipsum' will uncover many web sites still in their infancy. Various versions have evolved over the years, sometimes by accident, sometimes on purpose (injected humour and the like).</p>
      <p>Contrary to popular belief, Lorem Ipsum is not simply random text. It has roots in a piece of classical Latin literature from 45 BC, making it over 2000 years old. Daniel Whitcombe, a Latin professor at Harlow Ridge College in Vermont, looked up one of the more obscure Latin words, consectetur, from a Lorem Ipsum passage, and going through the cites of the word in classical literature, discovered the undoubtable source. Lorem Ipsum comes from sections 1.10.32 and 1.10.33 of "de Ordine Verborum Antiquorum" structures, to generate Lorem Ipsum which looks reasonable. The generated Lorem Ipsum is therefore always free from repetition, injected humour, or non-characteristic words etc.</p>
    </section>

    <div class="signature" role="img" aria-label="Handwritten signature"></div>

    <footer class="footer">
      <div class="contact-row">
        <span class="contact-item"><svg viewBox="0 0 10 10"><circle cx="5" cy="5" r="5" fill="#003E7C"/><path d="M5 2.2a1.8 1.8 0 0 1 1.8 1.8C6.8 5.4 5 7.8 5 7.8S3.2 5.4 3.2 4A1.8 1.8 0 0 1 5 2.2z" fill="#fff"/></svg>1870 Pembrook Blvd. Suite 400, Atlanta, GA 30127</span>
        <span class="contact-item"><svg viewBox="0 0 10 10"><circle cx="5" cy="5" r="5" fill="#003E7C"/><path d="M3.3 2.5l1 1-.6.8c.4.8 1 1.4 1.8 1.8l.8-.6 1 1-.7.9C4.7 7.2 2.8 5.3 2.6 3.2z" fill="#fff"/></svg>404.555.####</span>
        <span class="contact-item"><svg viewBox="0 0 10 10"><circle cx="5" cy="5" r="5" fill="#003E7C"/><rect x="2.8" y="3.6" width="4.4" height="3" fill="#fff"/><rect x="3.6" y="2.3" width="2.8" height="1.3" fill="#fff"/></svg>770.555.02##</span>
        <span class="contact-item"><svg viewBox="0 0 10 10"><circle cx="5" cy="5" r="5" fill="#003E7C"/><rect x="2.6" y="3.3" width="4.8" height="3.4" fill="#fff"/><path d="M2.6 3.3L5 5.2l2.4-1.9" stroke="#003E7C" stroke-width=".6" fill="none"/></svg>email@kestavoestates.com</span>
        <span class="contact-item"><svg viewBox="0 0 10 10"><circle cx="5" cy="5" r="5" fill="#003E7C"/><circle cx="5" cy="5" r="2.5" stroke="#fff" stroke-width=".6" fill="none"/><path d="M2.5 5h5M5 2.5c-1 1.4-1 3.6 0 5M5 2.5c1 1.4 1 3.6 0 5" stroke="#fff" stroke-width=".5" fill="none"/></svg>www.kestavoestates.com</span>
      </div>
      <div class="rule-thin"></div>
      <div class="rule-band"><span class="blue"></span><span class="black"></span></div>
    </footer>
  </main>
</body>
</html>
```